New Townhome community needs for sale sign.

need a 4 foot by 8 foot banner to put on building listing newly constructed townhomes as "coming soon" to market. Construction is scheduled to be completed Dec 2024. Sale of units will begin Spring of 2025.
6 individual townhome units each 2,000 square feet. each unit is 3 bedroom 2.5 bathroom with 2 car garage and each has a rooftop "sky lounge" with amazing views. Gated community. Units available for sale Spring of 2025. Real estate company selling units will be KTL & Associates. Will need KTL & Associates Logo on the banner. Would like to keep with the same blue color scheme as the KTL & Associates logo. phone number on banner to be 480-555-3164. web ktlpartners.example.

```html
<!DOCTYPE html>
<html lang="en">
<head>
<meta charset="utf-8">
<title>KTL &amp; Associates – Luxury Townhomes Coming Soon Banner</title>
<link href="https://fonts.googleapis.com/css2?family=Montserrat:wght@500;600;700;800;900&family=Bebas+Neue&family=Great+Vibes&display=swap" rel="stylesheet">
<style>
  :root {
    --page-bg: #ffffff;
    --banner-white: #ffffff;
    --sky-blue: #22a6d9;
    --panel-blue: #1f72a8;
    --panel-blue-deep: #185f8f;
    --fold-navy: #0b4a6f;
    --icon-blue: #1b69a2;
    --ink: #333333;
    --white: #ffffff;
  }
  * { margin: 0; padding: 0; box-sizing: border-box; }
  html, body {
    width: 966px;
    height: 1200px;
    overflow: hidden;
    background: var(--page-bg);
  }
  .banner {
    position: absolute;
    left: 33px;
    top: 375px;
    width: 900px;
    height: 450px;
    background: var(--banner-white);
    box-shadow: 0 4px 14px rgba(0,0,0,0.18);
    overflow: hidden;
    font-family: "Montserrat", sans-serif;
  }
  .banner-shapes {
    position: absolute;
    inset: 0;
  }
  .brand {
    position: absolute;
    left: 68px;
    top: 48px;
    display: flex;
    align-items: center;
    gap: 12px;
  }
  .brand-mark {
    width: 36px;
    height: 36px;
    background: var(--icon-blue);
  }
  .brand-name {
    font-family: "Montserrat", sans-serif;
    font-weight: 700;
    font-size: 30px;
    color: var(--ink);
    letter-spacing: -0.5px;
  }
  .headline {
    position: absolute;
    left: 33px;
    top: 140px;
    font-family: "Montserrat", sans-serif;
    font-weight: 900;
    font-size: 92px;
    line-height: 84px;
    color: var(--white);
    letter-spacing: -2px;
    text-transform: uppercase;
  }
  .phone {
    position: absolute;
    left: 31px;
    top: 345px;
    display: flex;
    align-items: center;
    gap: 20px;
  }
  .phone-icon { width: 46px; height: 46px; }
  .phone-number {
    font-family: "Bebas Neue", sans-serif;
    font-size: 64px;
    line-height: 1;
    color: var(--ink);
    padding-top: 6px;
  }
  .tagline-script {
    position: absolute;
    left: 548px;
    top: 12px;
    font-family: "Great Vibes", cursive;
    font-size: 96px;
    line-height: 1;
    color: var(--white);
  }
  .product {
    position: absolute;
    left: 582px;
    top: 110px;
    font-family: "Montserrat", sans-serif;
    font-weight: 800;
    font-size: 42px;
    color: var(--white);
    letter-spacing: -0.5px;
  }
  .sales-date {
    position: absolute;
    left: 520px;
    top: 168px;
    width: 358px;
    text-align: right;
    font-family: "Bebas Neue", sans-serif;
    font-size: 40px;
    line-height: 52px;
    color: var(--ink);
  }
  .features {
    position: absolute;
    top: 240px;
    list-style: none;
    font-family: "Montserrat", sans-serif;
    font-weight: 600;
    font-size: 15.5px;
    line-height: 24.7px;
    color: var(--white);
  }
  .features-left { left: 546px; }
  .features-right { left: 699px; }
  .features li {
    position: relative;
    padding-left: 17px;
  }
  .features li.continued { padding-left: 17px; }
  .features .tick {
    position: absolute;
    left: 0;
    top: 6px;
    width: 11px;
    height: 11px;
  }
  .features-divider {
    position: absolute;
    left: 681px;
    top: 243px;
    width: 0;
    height: 91px;
    border-left: 1.5px dashed rgba(255,255,255,0.8);
  }
  .website {
    position: absolute;
    left: 457px;
    top: 355px;
    width: 420px;
    text-align: right;
    font-family: "Montserrat", sans-serif;
    font-weight: 500;
    font-size: 30px;
    color: var(--white);
    letter-spacing: 0.3px;
  }
</style>
</head>
<body>
  <div class="banner">
    <svg class="banner-shapes" viewBox="0 0 900 450" width="900" height="450" aria-hidden="false">
      <defs>
        <linearGradient id="panelTone" x1="0" y1="0" x2="1" y2="1">
          <stop offset="0" stop-color="var(--panel-blue)"/>
          <stop offset="1" stop-color="var(--panel-blue-deep)"/>
        </linearGradient>
      </defs>
      <polygon points="508,0 900,0 900,450 393,450" fill="url(#panelTone)" role="img" aria-label="Faded photo of a furnished luxury townhome living room in blue tones"/>
      <polygon points="479,65 431,136 528,136" fill="var(--fold-navy)"/>
      <polygon points="0,136 528,136 482,318 0,318" fill="var(--sky-blue)"/>
      <polygon points="521,167 900,167 900,220 508,220" fill="var(--white)"/>
    </svg>

    <div class="brand">
      <span class="brand-mark"></span>
      <span class="brand-name">KTL &amp; Associates</span>
    </div>

    <h1 class="headline">Coming<br>Soon</h1>

    <div class="phone">
      <svg class="phone-icon" viewBox="0 0 46 46" aria-hidden="true">
        <circle cx="23" cy="23" r="23" fill="var(--icon-blue)"/>
        <path d="M16 13c1.2-.8 2.3-.6 3 .5l2 3.3c.6 1 .4 2-.5 2.7l-1.4 1c.9 2.2 2.6 4 4.8 5.1l1.1-1.4c.7-.9 1.7-1.1 2.7-.5l3.3 2c1.1.7 1.3 1.8.5 3l-1.2 1.6c-1 1.2-2.6 1.6-4.1 1-6.3-2.4-10.6-6.7-12.9-13-.5-1.5-.1-3.1 1.1-4.1z" fill="var(--white)"/>
        <path d="M25 12.5a8.5 8.5 0 0 1 8.5 8.5M25 16.5a4.5 4.5 0 0 1 4.5 4.5" stroke="var(--white)" stroke-width="1.8" fill="none" stroke-linecap="round"/>
      </svg>
      <span class="phone-number">480-555-3164</span>
    </div>

    <div class="tagline-script">Luxury</div>
    <div class="product">TOWNHOMES</div>
    <div class="sales-date">Sales Begin Spring 2025!</div>

    <ul class="features features-left">
      <li><svg class="tick" viewBox="0 0 12 12"><circle cx="6" cy="6" r="6" fill="var(--white)"/><path d="M3.3 6.2l1.8 1.8 3.6-3.6" stroke="var(--panel-blue)" stroke-width="1.6" fill="none"/></svg>6 Units</li>
      <li><svg class="tick" viewBox="0 0 12 12"><circle cx="6" cy="6" r="6" fill="var(--white)"/><path d="M3.3 6.2l1.8 1.8 3.6-3.6" stroke="var(--panel-blue)" stroke-width="1.6" fill="none"/></svg>2,000 sq. ft.</li>
      <li><svg class="tick" viewBox="0 0 12 12"><circle cx="6" cy="6" r="6" fill="var(--white)"/><path d="M3.3 6.2l1.8 1.8 3.6-3.6" stroke="var(--panel-blue)" stroke-width="1.6" fill="none"/></svg>3 Beds</li>
      <li><svg class="tick" viewBox="0 0 12 12"><circle cx="6" cy="6" r="6" fill="var(--white)"/><path d="M3.3 6.2l1.8 1.8 3.6-3.6" stroke="var(--panel-blue)" stroke-width="1.6" fill="none"/></svg>2.5 Baths</li>
    </ul>

    <div class="features-divider"></div>

    <ul class="features features-right">
      <li><svg class="tick" viewBox="0 0 12 12"><circle cx="6" cy="6" r="6" fill="var(--white)"/><path d="M3.3 6.2l1.8 1.8 3.6-3.6" stroke="var(--panel-blue)" stroke-width="1.6" fill="none"/></svg>2-Car Garage</li>
      <li><svg class="tick" viewBox="0 0 12 12"><circle cx="6" cy="6" r="6" fill="var(--white)"/><path d="M3.3 6.2l1.8 1.8 3.6-3.6" stroke="var(--panel-blue)" stroke-width="1.6" fill="none"/></svg>Rooftop</li>
      <li class="continued">"Sky Lounge"</li>
      <li><svg class="tick" viewBox="0 0 12 12"><circle cx="6" cy="6" r="6" fill="var(--white)"/><path d="M3.3 6.2l1.8 1.8 3.6-3.6" stroke="var(--panel-blue)" stroke-width="1.6" fill="none"/></svg>Gated Community</li>
    </ul>

    <div class="website">www.ktlpartners.example</div>
  </div>
</body>
</html>
```